Web Design Project for NFYL

Hi,
I am looking for a website design for the Northern Federation of Youth Listeners.
This is an organisation which helps with legal disputes and other challenges which involve children.  The company want a web page which is professional but friendly.  The purpose of the website is to explain what the organisation does and to give people a place where they can download documents and information.
The homepage will have a video on the page.  ALSO, we would prefer the site to have a left hand navigation (not a top navigation).
I have enclosed the logo, a picture of the old (rubbish) home page and a screenshot from the video (you are welcome to change the dimensions).
If you have any questions, please ask.
-D
UPDATE: 6th DECEMBER:
Thanks for the designs so far.  I promise to give feedback to every single person.  In the meantime, can I just say that there's some good designs so far but I don't think anyone has nailed this yet.
So, I am uploading a screenshot called "theylikethis.jpg".  This is a screenshot from a website that the client says they like.
Can I also say, it's okay to reduce the size of the video.  I'm seeing a lot of massive videos.
Thanks folks!
UPDATE:  You can view a live demo of the site that they like at www.demohostqv.co.uk
UPDATE:  I've just found another good example of a site with a left nav at www.brightpathresourcehub.com

Updates
Hi,
Hi folks,
Had a quick look at the designs and just to say how impressed I am with the qualityand choice. There are a few that caught my eye and I'll try and narrow them down.I've also passed the link onto the other representatives for their input beforemaking a final choice. If I don't hear from any of the other represenatatives by Wednesday, I'll chose adesign and let you know. Once again many thanks for the quick response in gettingdesigns done and really looking forward to seeing the completed website.
Industry/Entity Type
Legal
Requirements
Must have
- a video player (any size of your choosing)
a left side navigation
the logo

```html
<!DOCTYPE html>
<html lang="en">
<head>
<meta charset="utf-8">
<title>Northern Federation of Youth Listeners</title>
<link href="https://fonts.googleapis.com/css2?family=Yesteryear&family=PT+Serif:wght@400;700&family=PT+Sans:wght@400&display=swap" rel="stylesheet">
<style>
:root{
  --side-bg:#d9d9d9;
  --main-bg:#ececec;
  --text:#8c8c8c;
  --heading:#8e8e8e;
  --navy:#336699;
  --navy-dark:#24507d;
  --blue-edge:#1fc6f2;
  --green:#3a9a35;
  --green-edge:#1f5a1c;
  --orange:#f08e1a;
  --orange-edge:#6b3a08;
  --frame:#d6d6d6;
}
*{margin:0;padding:0;box-sizing:border-box}
html,body{width:1200px;height:773px;overflow:hidden}
body{position:relative;background:var(--main-bg);font-family:"PT Serif",Georgia,serif;color:var(--text)}
.sidebar{position:absolute;left:0;top:0;width:441px;height:773px;background:linear-gradient(90deg,#dcdcdc 0%,#d6d6d6 92%,#bdbdbd 100%)}
.main-bg{position:absolute;left:441px;top:0;right:0;height:773px;background:linear-gradient(90deg,#dedede 0,#eeeeee 30px,#efefef 100%)}
.abs{position:absolute}
.logo-ribbon{left:181px;top:0;width:172px;height:192px}
.logo-mark{left:232px;top:40px;width:70px;height:56px;display:flex;align-items:center;justify-content:center;font-family:"PT Sans",sans-serif;font-size:20px;color:#e8eef5}
.logo-name{left:181px;top:118px;width:172px;text-align:center;font-family:"PT Sans",sans-serif;font-size:15.5px;line-height:18px;color:#e3e8ee}
.search{left:150px;top:254px;width:234px;height:30px;border:1px solid #b8b8b8;border-radius:15px;background:#efefef;box-shadow:inset 0 1px 2px rgba(0,0,0,.12)}
.search span{position:absolute;left:19px;top:5px;font-style:italic;font-size:13.5px;color:#b0b0b0}
.search .btn{position:absolute;right:0;top:0;width:33px;height:28px;border-left:1px solid #c2c2c2;border-radius:0 15px 15px 0;background:#e2e2e2}
.side-h{left:151px;font-family:"Yesteryear",cursive;font-weight:400;font-size:22px;color:var(--heading);text-shadow:0 1px 0 #fff}
.rule{height:4px;border-top:1px solid #9a9a9a;border-bottom:1px solid #9a9a9a}
.side-rule{left:151px;width:233px}
.side-text{font-size:12.6px;line-height:16px;text-shadow:0 1px 0 #fff}
.about-text{left:151px;top:345px;width:150px}
.about-badge{left:310px;top:359px;width:74px;height:63px;background:#fff;border:1px solid #ccc;padding:5px}
.about-badge div{width:100%;height:100%;background:#0d3d8a;color:#fff;font-family:"PT Sans",sans-serif;font-size:17px;display:flex;align-items:center;justify-content:center}
.nav{left:151px;list-style:none}
.nav li{font-size:12.6px;line-height:15.8px;text-shadow:0 1px 0 #fff}
.home-tab{left:427px;top:68px;width:91px;height:30px}
.ribbon{width:137px;height:195px;left:456px}
.ribbon-text{position:absolute;left:0;width:137px;top:84px;text-align:center;color:#fff;font-size:12.8px;line-height:15.5px;text-shadow:0 1px 1px rgba(0,0,0,.35)}
.ornament{position:absolute;left:13px;top:13px;width:110px;height:50px;border-radius:6px;background:radial-gradient(ellipse at center,rgba(220,200,170,.85) 0,rgba(200,180,150,.35) 55%,rgba(0,0,0,0) 75%)}
.title{left:609px;top:64px;width:432px;font-family:"Yesteryear",cursive;font-weight:400;font-size:30px;color:var(--heading);text-shadow:0 1px 0 #fff;white-space:nowrap}
.title-rule{left:609px;top:113px;width:432px}
.video-frame{left:609px;top:140px;width:432px;height:276px;background:var(--frame);box-shadow:0 8px 6px -4px rgba(0,0,0,.25)}
.video-still{position:absolute;left:10px;top:9px;width:412px;height:259px;background:linear-gradient(180deg,#ece9e6 0%,#cdbfb5 45%,#a89a90 100%)}
.content{left:609px;width:432px;font-size:12.4px;line-height:15.8px;letter-spacing:-.1px;text-indent:19px;text-shadow:0 1px 0 #fff}
.footer{left:600px;top:698px;width:441px;height:34px;background:var(--navy);border-radius:6px;color:#fff;font-family:"PT Sans",sans-serif;font-size:12px;display:flex;align-items:center;justify-content:center}
</style>
</head>
<body>
<div class="sidebar"></div>
<div class="main-bg"></div>

<svg class="abs logo-ribbon" viewBox="0 0 172 192" aria-hidden="true">
  <defs><linearGradient id="rib" x1="0" y1="0" x2="0" y2="1"><stop offset="0" stop-color="#6e93bb"/><stop offset=".1" stop-color="#3c6b9c"/><stop offset="1" stop-color="#2f6296"/></linearGradient></defs>
  <path d="M0 0H172V184L166 190L160 184L154 190L148 184L142 190L136 184L130 190L124 184L118 190L112 184L106 190L100 184L94 190L88 184L82 190L76 184L70 190L64 184L58 190L52 184L46 190L40 184L34 190L28 184L22 190L16 184L10 190L4 184L0 188Z" fill="url(#rib)"/>
  <rect x="6" y="-2" width="160" height="182" fill="none" stroke="#fff" stroke-width="1.5" stroke-dasharray="4 3"/>
</svg>
<div class="abs logo-mark">NFYL</div>
<div class="abs logo-name">Northern Federation<br>of Youth<br>Listeners</div>

<div class="abs search"><span>search...</span><div class="btn">
  <svg width="33" height="28" viewBox="0 0 33 28"><circle cx="18.5" cy="12" r="6" fill="none" stroke="#8a8a8a" stroke-width="1.3"/><line x1="14.3" y1="16.3" x2="9.5" y2="21" stroke="#8a8a8a" stroke-width="1.6"/></svg>
</div></div>

<h2 class="abs side-h" style="top:304px">About Us</h2>
<div class="abs rule side-rule" style="top:337px"></div>
<p class="abs side-text about-text">Lorem ipsum dolor sit amet, consectetur adipiscing elit. Nam sed sem quis nunc viverra feugiat ac vel lorem.</p>
<div class="abs about-badge"><div>NFYL</div></div>

<h2 class="abs side-h" style="top:442px">Category</h2>
<div class="abs rule side-rule" style="top:475px"></div>
<ul class="abs nav" style="top:489px">
  <li>Home</li><li>About Us</li><li>News</li><li>Confrences</li><li>Minutes</li><li>Annual Reports</li><li>Archieve</li><li>Contact Us</li><li>Links</li>
</ul>

<h2 class="abs side-h" style="top:650px">Follow Us</h2>
<div class="abs rule side-rule" style="top:683px"></div>
<ul class="abs nav" style="top:697px">
  <li>Chatterline</li><li>Pagemates</li><li>My Corner</li>
</ul>

<svg class="abs home-tab" viewBox="0 0 91 30" aria-label="Home">
  <defs><linearGradient id="tab" x1="0" y1="0" x2="0" y2="1"><stop offset="0" stop-color="#5f8dbd"/><stop offset="1" stop-color="#2d5d90"/></linearGradient></defs>
  <polygon points="0,20 13,30 13,20" fill="#3c6b3b"/>
  <rect x="0" y="0" width="91" height="28" fill="url(#tab)" stroke="#dfe8f1" stroke-width="1.5"/>
  <text x="47" y="19" text-anchor="middle" font-family="PT Serif,serif" font-style="italic" font-weight="700" font-size="14" fill="#fff">Home</text>
</svg>

<div class="abs ribbon" style="top:137px">
  <svg width="137" height="195" viewBox="0 0 137 195"><path d="M2 2H135V164H124Q124 193 68.5 193Q13 193 13 164H2Z" fill="var(--navy)" stroke="var(--blue-edge)" stroke-width="3"/></svg>
  <div class="ornament" role="img" aria-label="Star ornament"></div>
  <p class="ribbon-text">Lorem ipsum<br>dolor sit amet,<br>consectetur<br>adipiscing elit.</p>
</div>
<div class="abs ribbon" style="top:344px">
  <svg width="137" height="195" viewBox="0 0 137 195"><path d="M2 2H135V164H124Q124 193 68.5 193Q13 193 13 164H2Z" fill="var(--green)" stroke="var(--green-edge)" stroke-width="3"/></svg>
  <div class="ornament" role="img" aria-label="Star ornament"></div>
  <p class="ribbon-text">Lorem ipsum<br>dolor sit amet,<br>consectetur<br>adipiscing elit.</p>
</div>
<div class="abs ribbon" style="top:548px">
  <svg width="137" height="195" viewBox="0 0 137 195"><path d="M2 2H135V164H124Q124 193 68.5 193Q13 193 13 164H2Z" fill="var(--orange)" stroke="var(--orange-edge)" stroke-width="3"/></svg>
  <div class="ornament" role="img" aria-label="Star ornament"></div>
  <p class="ribbon-text">Lorem ipsum<br>dolor sit amet,<br>consectetur<br>adipiscing elit.</p>
</div>

<h1 class="abs title">Northern Federation of Youth Listeners</h1>
<div class="abs rule title-rule"></div>

<div class="abs video-frame">
  <div class="video-still" role="img" aria-label="Video still of a presenter speaking to camera"></div>
  <svg class="abs" style="left:173px;top:96px" width="88" height="88" viewBox="0 0 88 88" aria-label="Play video">
    <circle cx="44" cy="44" r="43" fill="rgba(20,15,15,.82)"/>
    <polygon points="33,24 33,64 67,44" fill="#d8d8d8"/>
  </svg>
</div>

<p class="abs content" style="top:444px">Lorem ipsum dolor sit amet, consectetur adipiscing elit. Nam sed sem quis nunc viverra feugiat ac vel lorem. Praesent tortor mauris, dictum nec aliquam eget, congue non tellus. Integer tristique commodo neque sit amet laoreet. Nunc sit amet suscipit velit. Aenean consectetur est id dui varius dapibus. Etiam id purus lorem. Nullam ullamcorper vulputate gravida. Lorem ipsum dolor sit amet, consectetur adipiscing elit.</p>
<p class="abs content" style="top:557px">Proin metus sapien, vulputate sed malesuada at, bibendum eu erat. Duis consequat, sapien eget blandit eleifend, ipsum nisi pulvinar mi, nec aliquam erat lacus non turpis. Etiam eget ligula turpis, vitae pretium sapien. Nunc adipiscing porta volutpat. Integer vulputate mi sit amet libero laoreet nec vehicula urna iaculis. Cras sed turpis vel ante rhoncus vehicula at non mauris. Donec volutpat felis id dolor ornare auctor.</p>

<div class="abs footer">Copyright 2012 Website Name</div>
</body>
</html>
```